Reshape my sector - Site for startup to grow

Update: To clarify I've started a few wireframes: http://snipr.example/7qk3zWd this is by no means complete or even the layout im looking for, just some idea of the elements on the first few pages

This is for design only, I require PSDs as well high res versions of logo/other asset.

Concept

The site is place where Domain experts to identify real world problems in there respective industries that could be solved with software or hard ward products.

A similar site to this is : http://www.notionharbor.example/ which allows anyone to suggest ideas for products they want realising.

Pages needing design:

1) Login

2) Problems search: List of problems posted filterable by industry. Should contain:

- User who posted the problem (name, picture, etc)
- Title and short description of the problem space
- Current state of the project i.e. team created, just started, etc.

3) Problem details page, should contain:

- Title and large description of the problem space
- Optional image
- List of products that attempt to solve the problem (Name of product, short description, url)
- Discussion board (small forum for discussing the idea)
- List of teams started to solve the problem (show number of members and current state of the team, link to public team page)

4) Post a problem page:

- Form to create a problem containing all the things above

4) Public team page

- Shows team members (name, position, link to bio)
- List of team blog posts
- Adverts for team members, funding partners, beta testers etc

5) Private team page

- The ability to change the status of the project
- The ability to post blogs promoting there project
- The ability to advertise for additional team member, funding
partners, beta testers etc
- Private discussion board

The site will be called "www.reshapemysector.example" and will require a logo.

Target Market(s)

software developers, designers, entrepreneurs, VCs

Industry/Entity Type

Industry

Number of Pages Required

5+ page

Font styles to use
Serif
Sans Serif

Requirements
Must have
• PSDs + high res images
• Simple clean design see:
• - https://trial.velvetboards.example/
• - https://talk.quillnest.example/
• - https://pinmosaic.example/shots/4830517-Task-Panel/attachments/395208

```html
<!DOCTYPE html>
<html lang="en">
<head>
<meta charset="utf-8">
<title>Reshape My Sector – Post a Problem</title>
<link rel="stylesheet" href="https://fonts.googleapis.com/css2?family=Rajdhani:wght@700&family=Source+Sans+3:wght@400;600;700&display=swap">
<style>
:root{
  --green:#72c043;
  --orange:#f47a20;
  --ink:#2b2b2b;
  --muted:#7a7a7a;
  --panel:#f4f4f4;
  --footer:#e4e4e4;
  --white:#ffffff;
  --line:#333333;
  --ghost:#c4c4c4;
  --rule:#e2e2e2;
}
*{box-sizing:border-box;margin:0;padding:0}
html,body{width:1200px;height:676px;overflow:hidden}
body{position:relative;background:var(--panel);font-family:"Source Sans 3",Arial,sans-serif;color:var(--ink)}
.display{font-family:"Rajdhani","Arial Narrow",sans-serif;font-weight:700}
.site-header{position:absolute;left:0;top:0;width:1200px;height:61px;background:var(--green)}
.brand{position:absolute;left:27px;top:16px;font-size:25px;color:var(--white);line-height:1}
.nav-item{position:absolute;top:12px;width:90px;margin-left:-45px;text-align:center;color:var(--white);font-size:13px;line-height:1}
.nav-item svg{display:block;margin:0 auto 6px;height:22px}
.sidebar{position:absolute;left:0;top:61px;width:307px;height:615px;background:var(--white);border-right:1px solid var(--rule)}
.sidebar-notch{position:absolute;left:306px;top:74px}
.avatar{position:absolute;left:27px;top:22px;width:66px;height:66px;border-radius:50%;background:radial-gradient(circle at 50% 40%,#c98c6a,#6b4a38)}
.profile-name{position:absolute;left:102px;top:29px;font-size:16px;line-height:1}
.profile-role{position:absolute;left:102px;top:47px;font-size:11px;color:var(--ink)}
.profile-link{position:absolute;left:102px;top:68px;font-size:11px;font-weight:600;color:var(--green);line-height:18px}
.side-label{position:absolute;left:27px;font-size:12.5px;font-weight:600}
.side-field{position:absolute;left:27px;width:266px;border:1px solid var(--line);background:var(--white);font-size:12px;padding-left:9px}
.select{height:32px;line-height:30px}
.select::after{content:"";position:absolute;right:10px;top:12px;border:7px solid transparent;border-top:8px solid #9a9a9a;border-bottom:0}
.field-label{position:absolute;font-size:14px;font-weight:700;text-transform:uppercase;letter-spacing:.2px}
.box{position:absolute;border:2px solid var(--line);background:var(--white)}
.page-title{position:absolute;left:333px;top:86px;font-size:27px;color:var(--green);display:flex;align-items:center;gap:6px;line-height:1}
.toolbar{display:flex;height:25px;border-bottom:1px solid var(--line)}
.toolbar span{width:39px;border-right:1px solid var(--line);text-align:center;font-size:12px;line-height:25px}
.file{position:absolute;top:537px;width:60px;margin-left:-30px;text-align:center;font-size:10.5px}
.file svg{display:block;margin:0 auto 4px}
.submit{position:absolute;left:944px;top:537px;width:229px;height:52px;border-radius:7px;background:var(--orange);color:var(--white);font-size:14px;display:flex;align-items:center;justify-content:center;gap:8px}
.site-footer{position:absolute;left:307px;top:644px;width:893px;height:32px;background:var(--footer);font-size:10.5px;color:var(--muted);text-align:right;padding-right:27px;line-height:32px}
.site-footer b{font-weight:400;margin:0 6px}
</style>
</head>
<body>
<header class="site-header">
  <div class="brand display">Reshape My Sector</div>
  <div class="nav-item display" style="left:896px">
    <svg viewBox="0 0 24 22" width="26"><path d="M12 1 23 21H1Z" fill="#fff"/><rect x="10.8" y="7" width="2.4" height="8" fill="#72c043"/><rect x="10.8" y="16.5" width="2.4" height="2.4" fill="#72c043"/></svg>PROBLEMS</div>
  <div class="nav-item display" style="left:972px">
    <svg viewBox="0 0 24 22" width="24"><rect x="1" y="1" width="22" height="20" fill="#fff"/><rect x="4" y="4" width="7" height="6" fill="#72c043"/><rect x="13" y="4" width="7" height="2" fill="#72c043"/><rect x="13" y="8" width="7" height="2" fill="#72c043"/><rect x="4" y="12" width="16" height="2" fill="#72c043"/><rect x="4" y="16" width="16" height="2" fill="#72c043"/></svg>NEWS</div>
  <div class="nav-item display" style="left:1044px">
    <svg viewBox="0 0 24 22" width="24"><rect x="1" y="4" width="22" height="15" fill="#fff"/><path d="M1 4 12 13 23 4" fill="none" stroke="#72c043" stroke-width="2"/></svg>CONTACT</div>
  <div class="nav-item display" style="left:1138px">
    <svg viewBox="0 0 24 22" width="24"><circle cx="12" cy="6" r="5.5" fill="#fff"/><path d="M2 22c0-7 4-9 10-9s10 2 10 9Z" fill="#fff"/></svg>MY ACCOUNT</div>
</header>

<aside class="sidebar">
  <div class="avatar" role="img" aria-label="Profile photo of the member"></div>
  <div class="profile-name display">Alan Marsh</div>
  <div class="profile-role">Chief Scientist at Northfield Tech</div>
  <div class="profile-link">ProfileNet</div>

  <div class="side-label" style="top:106px">Your expereince of the problem:</div>
  <div class="side-field select" style="top:126px">10+ Years</div>
  <div class="side-label" style="top:170px">Your background:</div>
  <div class="side-field" style="top:190px;height:133px"></div>
  <div class="side-label" style="top:335px">Your involvement:</div>
  <div class="side-field select" style="top:355px">I just want someone to solve it</div>
</aside>
<svg class="sidebar-notch" width="18" height="56" viewBox="0 0 18 56"><path d="M0 0 16 28 0 56Z" fill="#fff" stroke="#e2e2e2"/><rect x="0" y="0" width="1.5" height="56" fill="#fff"/></svg>

<main>
  <h1 class="page-title display">
    <svg viewBox="0 0 24 22" width="27" height="25"><path d="M12 1 23 21H1Z" fill="#72c043"/><rect x="10.8" y="7" width="2.4" height="8" fill="#fff"/><rect x="10.8" y="16.5" width="2.4" height="2.4" fill="#fff"/></svg>PROBLEM</h1>

  <div class="field-label" style="left:333px;top:128px">Title:</div>
  <div class="box" style="left:333px;top:146px;width:413px;height:39px"></div>
  <div class="field-label" style="left:760px;top:128px">Industry:</div>
  <div class="box" style="left:760px;top:146px;width:413px;height:39px"></div>

  <div class="field-label" style="left:333px;top:203px">Elivator pitch:</div>
  <div class="box" style="left:333px;top:221px;width:840px;height:80px"></div>

  <div class="field-label" style="left:333px;top:319px">Detailed prolem description:</div>
  <div class="box" style="left:333px;top:337px;width:840px;height:159px">
    <div class="toolbar">
      <span>h1</span><span>h2</span><span>h3</span><span>h4</span><span>h5</span><span>h6</span><span>p</span><span><i>i</i></span><span><b>b</b></span><span><u>U</u></span>
    </div>
  </div>

  <div class="field-label" style="left:333px;top:515px">Files:</div>
  <div class="file" style="left:367px">
    <svg width="40" height="53" viewBox="0 0 40 53"><path d="M1 1H29L39 11V52H1Z" fill="#fff" stroke="#333" stroke-width="2"/><path d="M29 1V11H39" fill="none" stroke="#333" stroke-width="2"/><text x="20" y="31" font-size="8" font-weight="700" text-anchor="middle" font-family="Source Sans 3,sans-serif">.docx</text></svg>Wireframe</div>
  <div class="file" style="left:433px">
    <svg width="40" height="53" viewBox="0 0 40 53"><path d="M1 1H29L39 11V52H1Z" fill="#fff" stroke="#333" stroke-width="2"/><path d="M29 1V11H39" fill="none" stroke="#333" stroke-width="2"/><text x="20" y="31" font-size="8" font-weight="700" text-anchor="middle" font-family="Source Sans 3,sans-serif">.html</text></svg>Deck</div>
  <div class="file" style="left:500px">
    <svg width="40" height="53" viewBox="0 0 40 53"><path d="M1 1H29L39 11V52H1Z" fill="#fff" stroke="#c4c4c4" stroke-width="2"/><path d="M29 1V11H39" fill="none" stroke="#c4c4c4" stroke-width="2"/><path d="M20 24V38M13 31H27" stroke="#c4c4c4" stroke-width="3"/></svg></div>

  <div class="submit display">
    <svg width="20" height="18" viewBox="0 0 20 18"><path d="M0 8 20 0 15 18 10 12 17 3 7 10Z" fill="#fff"/></svg>Submit Problem for Approval</div>
</main>

<footer class="site-footer">FAQs<b>|</b>About Us<b>|</b>Privacy<b>|</b>Terms<b>|</b>©2016 Reshape My Sector.</footer>
</body>
</html>
```